Broschüren-Design für Produzent von hochwertigen Verpackungs- und Präsentationslösungen
Zielgruppe
Wir produzieren hochwertige Verpackungs- und Präsentationslösungen.
Unsere Zielgruppe sind Firmen, welche kreative Premium-Packaging benötigt.
Aufgabenstellung
- Format: A4 hoch
- Umfang: 6 Seiten
- Falzart: Wickelfalz
- Design muss sehr hochwertig sein. Passend zu unseren Produktion (siehe Bilder)
- Wir möchten mit diesem Falzprospekt eine Übersicht über unsere Produkte generieren.
- Die Produkte sind bereits schon hochwertig fotografiert und müssen in einem anspruchsvollen Design in Szene gesetzt werden.
- Der Prospekt sollte die Kunden emotional berühren.
- Auf der Titelseite werden wir den Titel «High Performance Packaging» mit Folien prägen
- Seitenaufbau gemäss meiner Visualisierung (im Anhang)
- Bei jeder Produktkategorie möchte ich ein Grosses Übersichtsbild zusammen mit einem kurzen Text.
Ergänzend können noch weitere (passende) Bilder der jeweiligen Kategorie abgebildet werden.
Im Anhang finden Sie:
- Visualisierung des zu gestaltenden Prospekt
- Werbeflyer (zur Ansicht/Inspiration). In etwa so stellen wir uns das Design/Tonalität vor.
- Weitere passende Produktbilder können vorerst auf der Webseite unseres Produktionspartner (www.bogenhaus-muster.de) entnommen werden.

```html
<!DOCTYPE html>
<html lang="de">
<head>
<meta charset="utf-8">
<title>Feinkarton Studio – Falzprospekt Aussenseite</title>
<link href="https://fonts.googleapis.com/css2?family=Fira+Sans:wght@300;400;500&family=Playfair+Display:ital,wght@1,900&display=swap" rel="stylesheet">
<style>
  :root{
    --slate:#3f4453;
    --slate-deep:#363a47;
    --copper:#dc8a5b;
    --paper:#ffffff;
    --ink:#3f4453;
    --ink-soft:#4b5060;
    --on-dark:#f2f2f4;
    --fold:#8a3a4a;
  }
  *{margin:0;padding:0;box-sizing:border-box}
  html,body{width:1200px;height:566px;overflow:hidden;background:var(--paper)}
  body{font-family:"Fira Sans",sans-serif;position:relative}
  .panel{position:absolute;top:0;height:566px}
  .panel--inner{left:0;width:396px;background:var(--paper)}
  .panel--back{left:396px;width:402px;background:var(--slate)}
  .panel--cover{left:798px;width:402px;background:var(--slate);border-left:1px solid var(--fold)}

  .intro{position:absolute;left:48px;top:44px;width:300px;color:var(--ink)}
  .intro__title{font-weight:500;font-size:14px;line-height:18px;letter-spacing:.2px}
  .intro__text{margin-top:12px;font-weight:300;font-size:8px;line-height:13.5px;color:var(--ink-soft)}
  .intro__text p+p{margin-top:5px}

  .eco{position:absolute;left:48px;top:202px;width:301px;height:316px;background:var(--slate);color:var(--on-dark);padding:20px 25px}
  .eco__title{font-weight:400;font-size:11px;letter-spacing:.2px}
  .eco__lead{margin-top:8px;font-weight:300;font-size:8px;line-height:13.5px;width:230px}
  .eco__list{list-style:none;margin-top:32px}
  .eco__item{display:flex;align-items:flex-start;height:62px}
  .eco__icon{width:43px;height:43px;border-radius:50%;background:var(--copper);flex:none;display:flex;align-items:center;justify-content:center}
  .eco__body{margin-left:29px;margin-top:1px;font-weight:300;font-size:8px;line-height:13.5px}
  .eco__body strong{display:block;font-weight:500}

  .contact{position:absolute;left:155px;top:446px;display:flex;color:var(--on-dark)}
  .brand-mark{width:34px;height:34px;border-radius:50%;background:var(--on-dark);margin-top:6px}
  .contact__lines{margin-left:24px;font-weight:300;font-size:8px;line-height:13.5px}
  .contact__name{font-weight:500}
  .contact__owner{margin-top:13px}

  .product-photo{position:absolute;left:42px;top:112px;width:360px;height:210px;background:linear-gradient(135deg,#6e5446 0%,#4d4c58 55%,#7b7f92 100%);border-radius:2px}
  .badge{position:absolute;left:272px;top:33px;width:97px;height:97px;border-radius:50%;background:var(--copper);display:flex;align-items:center;justify-content:center;text-align:center}
  .badge__text{font-family:"Playfair Display",serif;font-style:italic;font-weight:900;font-size:14px;line-height:17px;color:var(--slate);transform:rotate(-8deg)}
  .cover__title{position:absolute;left:47px;top:334px;font-family:"Playfair Display",serif;font-style:italic;font-weight:900;font-size:44px;line-height:47px;color:var(--copper);letter-spacing:-.3px}
  .cover__sub{position:absolute;left:48px;top:508px;font-weight:300;font-size:10.5px;color:var(--on-dark);letter-spacing:.2px}
</style>
</head>
<body>
  <section class="panel panel--inner">
    <div class="intro">
      <h2 class="intro__title">Höchste Qualität<br>zu unschlagbaren Preisen.</h2>
      <div class="intro__text">
        <p>Mit einer unvergleichlich grossen Bandbreite im Bereich des Premium Packaging bieten wir vielseitige Verpackungs- und Präsentationslösungen.</p>
        <p>Einzigartiges Design, variable Firmen und hochwertige Haptik unterstreichen die Bedeutung von Ihren Produkten.</p>
        <p>Überzeugen Sie sich jetzt und bestellen Sie Ihr individuelles Angebot!</p>
      </div>
    </div>

    <div class="eco">
      <h3 class="eco__title">Nachhaltige Papiere als Standard</h3>
      <p class="eco__lead">Bei uns gehen neuste Technologien und Umweltschutz Hand in Hand. Wir setzen auf nachhaltige Materialien und eine emissionsarme Produktion.</p>
      <ul class="eco__list">
        <li class="eco__item">
          <span class="eco__icon">
            <svg width="30" height="30" viewBox="0 0 30 30" fill="none" stroke="#fff" stroke-width="1">
              <path d="M4 22 L9 8 L14 22 Z M11 22 L16 5 L21 22 Z M18 22 L23 9 L28 22 Z"/>
              <path d="M9 22v4 M16 22v4 M23 22v4 M2 26h26"/>
            </svg>
          </span>
          <div class="eco__body"><strong>Nachhaltige Papiere</strong>Unsere Rohstoffe stammen aus nachhaltiger<br>Forstwirtschaft.</div>
        </li>
        <li class="eco__item">
          <span class="eco__icon">
            <svg width="26" height="30" viewBox="0 0 26 30" fill="none" stroke="#fff" stroke-width="1">
              <path d="M13 2 L24 6 V15 C24 21 19 25 13 28 C7 25 2 21 2 15 V6 Z"/>
              <path d="M13 5 L21 8 V15 C21 19.5 17.5 22.5 13 25 C8.5 22.5 5 19.5 5 15 V8 Z"/>
              <path d="M9 15 L12 18 L17 12"/>
            </svg>
          </span>
          <div class="eco__body"><strong>Wiederverwendbarkeit</strong>Unsere Boxen sind so schön und stabil,<br>dass man sie auf jeden Fall wiederverwendet.</div>
        </li>
        <li class="eco__item">
          <span class="eco__icon">
            <svg width="30" height="30" viewBox="0 0 30 30" fill="none" stroke="#fff" stroke-width="1.1" stroke-linejoin="round">
              <path d="M10 11 L14 4 H18 L21 9"/>
              <path d="M19 9 L23 10 L24 6"/>
              <path d="M23 15 L27 22 L25 26 H19"/>
              <path d="M21 24 L18 26 L21 28"/>
              <path d="M12 26 H5 L3 22 L6 16"/>
              <path d="M4 17 L7 14 L9 17"/>
            </svg>
          </span>
          <div class="eco__body"><strong>Recyclebare Lösungen</strong>Auf Nachfrage können wir Ihnen eine<br>100% recyclebare Verpackung anbieten.</div>
        </li>
      </ul>
    </div>
  </section>

  <section class="panel panel--back">
    <div class="contact">
      <span class="brand-mark" aria-hidden="true"></span>
      <div class="contact__lines">
        <div class="contact__name">feinkarton-studio.ch</div>
        <div>hallo@feinkarton-studio.ch</div>
        <div>041 555 01 23</div>
        <div class="contact__owner">Eine Marke von Riedhalde Medien AG.</div>
      </div>
    </div>
  </section>

  <section class="panel panel--cover">
    <div class="product-photo" role="img" aria-label="Produktfoto: kupferfarbene Ordnerbox und anthrazitfarbene Schubladenbox mit Kupfergriffen"></div>
    <div class="badge"><span class="badge__text">Mappen,<br>Ordner &amp;<br>mehr</span></div>
    <h1 class="cover__title">High<br>Performance<br>Packaging</h1>
    <p class="cover__sub">Exklusive Verpackungs- und Präsentationslösungen</p>
  </section>
</body>
</html>
```